BRISKLAND ELECTRICAL SIGN

We are wanting a sign to mount on the side of the road to attract peoples attention, it will be 1200mm high by 2400mm wide. We want it to stand out from the others, modern sharp looking, We are an electrical contractor who wants to be the market leader and supplier of choice to our current clients and futre clients.

Industry/Entity Type

Electrical

Colors

Designer to choose colors to be used in the design.

Requirements
Must have
• Name: Briskland Electrical
• Our logo as per uploaded files
• The words: Design - Installation - Maintenance
• Freecall: 0800 392 548
• Mobile : 021 947 3152 (delete mobile number if gets to cluttered)
• Web: www.briskland.net.nz
Should not have
• a light bulb, or plug

```html
<!DOCTYPE html>
<html lang="en">
<head>
<meta charset="utf-8">
<title>Briskland Electrical – Roadside Sign</title>
<link href="https://fonts.googleapis.com/css2?family=Lato:wght@700;900&family=Nunito:wght@700;800&display=swap" rel="stylesheet">
<style>
  :root {
    --navy: #070a2e;
    --sky: #5fc4f0;
    --brand-blue: #3b78c4;
    --deep-blue: #1f3f86;
    --lime: #8cc63f;
    --white: #ffffff;
    --rule: #6a6f8c;
  }
  html, body {
    margin: 0;
    padding: 0;
    width: 1200px;
    height: 1200px;
    overflow: hidden;
    background: var(--white);
  }
  .sign {
    position: relative;
    width: 1200px;
    height: 1200px;
    overflow: hidden;
    background: var(--white);
    font-family: "Nunito", "Helvetica Neue", Arial, sans-serif;
  }
  .sign__bands {
    position: absolute;
    inset: 0;
    width: 1200px;
    height: 1200px;
  }
  .panel {
    position: absolute;
    left: 0;
    width: 1200px;
    text-align: center;
  }
  .brand-name {
    margin: 0;
    font-family: "Nunito", "Helvetica Neue", Arial, sans-serif;
    font-weight: 800;
    line-height: 1;
    letter-spacing: 2px;
  }
  .brand-name__main { display: block; }
  .brand-name__sub { display: block; letter-spacing: 3px; }

  .panel--dark .brand-name { color: var(--white); }
  .panel--dark .brand-name__main { font-size: 104px; }
  .panel--dark .brand-name__sub { font-size: 42px; margin-top: 10px; padding-left: 260px; }

  .panel--light .brand-name { color: var(--brand-blue); }
  .panel--light .brand-name__main { font-size: 150px; }
  .panel--light .brand-name__sub { font-size: 62px; margin-top: 10px; padding-left: 380px; }

  .services {
    margin: 0;
    font-family: "Nunito", "Helvetica Neue", Arial, sans-serif;
    font-weight: 700;
    font-size: 44px;
  }
  .panel--dark .services { color: var(--sky); }
  .panel--light .services { color: var(--deep-blue); }

  .divider {
    width: 780px;
    height: 2px;
    margin: 0 auto;
    background: linear-gradient(90deg, transparent, var(--rule), transparent);
  }
  .contact {
    font-family: "Lato", "Helvetica Neue", Arial, sans-serif;
    font-weight: 700;
    display: flex;
    align-items: center;
    justify-content: center;
  }
  .panel--dark .contact { color: var(--sky); }
  .contact--phones { font-size: 60px; gap: 14px; }
  .contact--web { font-size: 56px; gap: 14px; }
  .contact__sep { margin: 0 14px 0 28px; }
  .icon-badge { width: 56px; height: 56px; flex: none; }

  .contact-list {
    position: absolute;
    left: 72px;
    font-family: "Lato", "Helvetica Neue", Arial, sans-serif;
    font-weight: 900;
    color: var(--deep-blue);
  }
  .contact-list__row {
    display: flex;
    align-items: center;
    gap: 10px;
    font-size: 32px;
    height: 52px;
  }
  .contact-list__icon { width: 34px; height: 34px; flex: none; }
</style>
</head>
<body>
<main class="sign">

  <svg class="sign__bands" viewBox="0 0 1200 1200" aria-hidden="true">
    <rect x="0" y="0" width="1200" height="600" fill="var(--navy)"/>
    <polygon points="0,600 1200,600 1200,612 0,648" fill="var(--brand-blue)"/>
    <polygon points="0,648 1200,612 1200,618 0,660" fill="var(--lime)"/>
    <polygon points="0,1200 0,1188 1200,1146 1200,1200" fill="var(--lime)"/>
    <polygon points="300,1180 1200,1146 1200,1154 300,1186" fill="var(--brand-blue)"/>
  </svg>

  <section class="panel panel--dark" style="top:0;height:600px;">
    <h1 class="brand-name" style="position:absolute;left:0;right:0;top:130px;">
      <span class="brand-name__main">BRISKLAND</span>
      <span class="brand-name__sub">ELECTRICAL</span>
    </h1>
    <p class="services" style="position:absolute;left:0;right:0;top:333px;">Design | Installation | Maintenance</p>
    <div class="divider" style="position:absolute;left:210px;top:416px;"></div>
    <div class="contact contact--phones" style="position:absolute;left:0;right:0;top:440px;">
      <svg class="icon-badge" viewBox="0 0 56 56" aria-hidden="true">
        <circle cx="28" cy="28" r="28" fill="var(--white)"/>
        <path d="M19 15c2-1 4 0 5 2l2 5c0 2-1 3-2 4 1 3 4 6 7 7 1-1 2-2 4-2l5 2c2 1 3 3 2 5-1 3-4 4-7 3-9-2-16-9-18-18-1-3 0-6 2-8z" fill="var(--navy)"/>
      </svg>
      <span>0800 392 548</span>
      <span class="contact__sep">|</span>
      <svg class="icon-badge" viewBox="0 0 56 56" aria-hidden="true">
        <circle cx="28" cy="28" r="28" fill="var(--white)"/>
        <rect x="19" y="11" width="18" height="34" rx="3" fill="var(--navy)"/>
        <rect x="21.5" y="15" width="13" height="23" fill="var(--white)"/>
        <circle cx="28" cy="41.5" r="1.8" fill="var(--white)"/>
      </svg>
      <span>021 947 3152</span>
    </div>
    <div class="contact contact--web" style="position:absolute;left:0;right:0;top:517px;">
      <svg class="icon-badge" viewBox="0 0 56 56" aria-hidden="true">
        <circle cx="28" cy="28" r="28" fill="var(--white)"/>
        <g fill="none" stroke="var(--navy)" stroke-width="2.2">
          <circle cx="28" cy="28" r="15"/>
          <ellipse cx="28" cy="28" rx="6.5" ry="15"/>
          <line x1="13" y1="28" x2="43" y2="28"/>
          <path d="M15.5 20h25M15.5 36h25"/>
        </g>
      </svg>
      <span>www.briskland.net.nz</span>
    </div>
  </section>

  <section class="panel panel--light" style="top:660px;height:540px;">
    <h2 class="brand-name" style="position:absolute;left:0;right:0;top:65px;">
      <span class="brand-name__main">BRISKLAND</span>
      <span class="brand-name__sub">ELECTRICAL</span>
    </h2>
    <p class="services" style="position:absolute;left:0;right:0;top:326px;">Design | Installation | Maintenance</p>
  </section>

  <div class="contact-list" style="top:1062px;">
    <div class="contact-list__row">
      <svg class="contact-list__icon" viewBox="0 0 34 34" aria-hidden="true">
        <path d="M8 4c2-1 3 0 4 2l2 4c0 2-1 3-2 4 1 3 4 6 7 7 1-1 2-2 4-2l4 2c2 1 2 3 1 4-1 3-4 4-7 3-8-2-14-8-16-16-1-3 0-6 3-8z" fill="var(--brand-blue)"/>
      </svg>
      <span>0800 392 548</span>
    </div>
    <div class="contact-list__row">
      <svg class="contact-list__icon" viewBox="0 0 34 34" aria-hidden="true">
        <g fill="none" stroke="var(--brand-blue)" stroke-width="2.2">
          <circle cx="17" cy="17" r="14"/>
          <ellipse cx="17" cy="17" rx="6" ry="14"/>
          <line x1="3" y1="17" x2="31" y2="17"/>
          <path d="M5.5 10h23M5.5 24h23"/>
        </g>
      </svg>
      <span>www.briskland.net.nz</span>
    </div>
  </div>

</main>
</body>
</html>
```